Stone & Sky Subtitle Walk Toward Quiet Grace

This is a spiritual book. It opens with a question for the readers -- Are you happy? Then proceeds to discuss the meaning of happiness, why the majority isn't and ways to achieve it. The work offers hope, and actual answers. In that regard the cover needs to relate those things.

I'm happy to contribute by answering further questions and making suggestions, however, am open to the designer letting their Spirit soar and see where it leads them.

Ask yourself the question; Am I happy, imagine finding Your happiness then designing the cover that comes from that space. Just a thought.

```html
<!DOCTYPE html>
<html lang="en">
<head>
<meta charset="utf-8">
<title>Stone &amp; Sky – Book Cover</title>
<link rel="stylesheet" href="https://fonts.googleapis.com/css2?family=Cinzel:wght@400&family=Oswald:wght@300;400&family=Source+Sans+3:wght@400;600&display=swap">
<style>
  :root {
    --ink-deep: #12151d;
    --ink-mid: #2a303d;
    --ink-black: #000000;
    --mist: rgba(205, 215, 232, 0.55);
    --mist-soft: rgba(170, 185, 210, 0.25);
    --white: #ffffff;
    --shadow: rgba(0, 0, 0, 0.85);
    --wing-dark: #5a2a08;
    --wing-mid: #c06a1c;
    --wing-light: #e8a54a;
  }
  * { margin: 0; padding: 0; box-sizing: border-box; }
  html, body { width: 1200px; height: 900px; overflow: hidden; background: var(--ink-deep); }
  .cover {
    position: relative;
    width: 1200px;
    height: 900px;
    overflow: hidden;
    color: var(--white);
    background:
      radial-gradient(ellipse 700px 500px at 300px 500px, rgba(70, 80, 100, 0.45), transparent 70%),
      linear-gradient(180deg, var(--ink-deep) 0%, var(--ink-mid) 55%, #1d2230 100%);
  }

  /* Flowing light art */
  .light-flow {
    position: absolute;
    left: 0;
    top: 440px;
    width: 1200px;
    height: 460px;
    background:
      radial-gradient(ellipse 420px 150px at 980px 250px, var(--mist), transparent 70%),
      radial-gradient(ellipse 560px 110px at 860px 360px, var(--mist), transparent 72%),
      radial-gradient(ellipse 600px 80px at 330px 400px, var(--mist-soft), transparent 75%),
      radial-gradient(ellipse 260px 120px at 1160px 120px, var(--mist-soft), transparent 70%);
  }

  /* Back cover */
  .back-copy {
    position: absolute;
    left: 40px;
    width: 480px;
    text-align: center;
    font-family: "Source Sans 3", sans-serif;
    font-size: 17.5px;
    line-height: 24px;
  }
  .back-copy.blurb { top: 172px; }
  .back-copy.blurb p + p { margin-top: 24px; }
  .back-copy.profile { top: 586px; }
  .profile-heading { font-size: 17.5px; font-weight: 400; margin-bottom: 12px; text-transform: uppercase; }
  .barcode-box {
    position: absolute;
    left: 412px;
    top: 828px;
    width: 110px;
    height: 54px;
    background: var(--white);
    color: var(--ink-black);
    font-family: "Source Sans 3", sans-serif;
    font-weight: 600;
    font-size: 21px;
    line-height: 24px;
    text-align: center;
    padding-top: 3px;
  }

  /* Spine */
  .spine-title {
    position: absolute;
    left: 562px;
    top: 64px;
    writing-mode: vertical-rl;
    white-space: nowrap;
    font-family: "Cinzel", serif;
    font-size: 40px;
    text-shadow: 2px 2px 3px var(--shadow);
  }
  .spine-subtitle { font-family: "Oswald", sans-serif; font-weight: 300; font-size: 40px; letter-spacing: 1px; }
  .spine-author {
    position: absolute;
    left: 540px;
    width: 96px;
    top: 822px;
    text-align: center;
    font-family: "Cinzel", serif;
    font-size: 19px;
    line-height: 32px;
  }

  /* Front cover */
  .butterfly-art {
    position: absolute;
    left: 722px;
    top: 82px;
    width: 140px;
    height: 172px;
    border-radius: 60% 45% 50% 55%;
    background: radial-gradient(ellipse at 55% 45%, var(--wing-light), var(--wing-mid) 55%, var(--wing-dark) 100%);
    box-shadow: 6px 8px 14px var(--shadow);
  }
  .front-title {
    position: absolute;
    left: 660px;
    width: 520px;
    top: 270px;
    text-align: center;
    font-family: "Cinzel", serif;
    font-weight: 400;
    font-size: 74px;
    line-height: 100px;
    white-space: nowrap;
    text-shadow: 4px 4px 5px var(--shadow);
  }
  .front-title .amp { font-size: 44px; }
  .title-rule {
    position: absolute;
    left: 678px;
    top: 380px;
    width: 482px;
    height: 3px;
    background: var(--white);
    box-shadow: 2px 2px 3px var(--shadow);
  }
  .front-subtitle {
    position: absolute;
    left: 660px;
    width: 520px;
    top: 396px;
    text-align: center;
    font-family: "Oswald", sans-serif;
    font-weight: 300;
    font-size: 42px;
    line-height: 50px;
    letter-spacing: 1px;
    text-transform: uppercase;
    text-shadow: 3px 3px 4px var(--shadow);
  }
  .front-author {
    position: absolute;
    left: 660px;
    width: 520px;
    top: 810px;
    text-align: center;
    font-family: "Oswald", sans-serif;
    font-weight: 300;
    font-size: 40px;
    letter-spacing: 3px;
    text-shadow: 3px 3px 4px var(--shadow);
  }
</style>
</head>
<body>
<main class="cover">
  <div class="light-flow" role="img" aria-label="Flowing ribbons of silvery light sweeping across the lower cover"></div>

  <section class="back-copy blurb">
    <p>This is a spiritual book. It opens with a question for the readers -- Are you happy? Then proceeds to discuss the meaning of happiness, why the majority isn't and ways to achieve it. The work offers hope, and actual answers. In that regard the cover needs to relate those things.</p>
    <p>I'm happy to contribute by answering further questions and making suggestions, however, am open to the designer letting their Spirit soar and see where it leads them</p>
  </section>

  <section class="back-copy profile">
    <h2 class="profile-heading">Author's Profile</h2>
    <p>Ask yourself the question; Am I happy, imagine finding Your happiness then designing the cover that comes from that space. Just a thought.</p>
  </section>

  <div class="barcode-box">BAR<br>CODE</div>

  <div class="spine-title">STONE&amp;SKY: <span class="spine-subtitle">WALK TOWARD QUIET GRACE</span></div>
  <div class="spine-author">OWEN<br>CALDER</div>

  <div class="butterfly-art" role="img" aria-label="Illustration of an orange monarch butterfly resting with wings closed"></div>

  <h1 class="front-title">STONE<span class="amp">&amp;</span>SKY</h1>
  <div class="title-rule"></div>
  <p class="front-subtitle">Walk Toward Quiet<br>Grace</p>
  <p class="front-author">OWEN CALDER</p>
</main>
</body>
</html>
```